Holvery Real Estate Management Consulting

To design a high end company profile that inspires confidence in high net worth individuals and similar clients. The profile to include real estate images, preferably real images. The firm is a Zambian firm and has its target to be comparable to Tesk & Company, Parlowe & Company, Wilder Osten, Lun dorv pelsin wilder osten, TLAV Real estate company as such.

Target Market(s)

Real estate clients such as high net worth individuals, private and public companies, government and international agencies, banks and insurance companies, trusts and pension funds and individual investors. the sub target market group being developers, planners, financiers, market analysts, designers, economists, engineers, architects, construction managers, quantity surveyors and public officials and others

Colors

Designer to choose colors to be used in the design.

Requirements
Must have
• Company logo

```html
<!DOCTYPE html>
<html lang="en">
<head>
<meta charset="utf-8">
<title>Holvery Real Estate – Company Profile Cover</title>
<link rel="stylesheet" href="https://fonts.googleapis.com/css2?family=Lato:wght@400;700;900&display=swap">
<style>
  :root {
    --stage: #2a2a2c;
    --navy: #2e3d93;
    --blue: #3b4fa8;
    --band-light: #5a6cc0;
    --sky: #5fb2e2;
    --paper: #f4f5fa;
    --paper-shade: #e4e7f2;
    --grey: #7c7c82;
    --text-dark: #5a5a62;
    --white: #ffffff;
  }
  * { margin: 0; padding: 0; box-sizing: border-box; }
  html, body {
    width: 1200px; height: 789px; overflow: hidden;
    background: var(--stage);
    font-family: "Lato", sans-serif;
  }
  .spread {
    position: absolute; left: 105px; top: 45px;
    width: 990px; height: 700px;
  }
  .spread-art { position: absolute; inset: 0; }
  .text { position: absolute; }

  .brand-mark {
    font-weight: 900; letter-spacing: 2px; line-height: 1;
  }
  .back-mark { left: 350px; top: 360px; font-size: 54px; color: var(--white); }

  .contact { left: 0; width: 495px; top: 566px; text-align: center; }
  .contact-title { color: var(--navy); font-weight: 700; font-size: 16px; margin-bottom: 6px; }
  .contact-address { color: var(--text-dark); font-size: 11.5px; line-height: 1.35; margin-bottom: 10px; }
  .contact-lines { color: var(--navy); font-size: 12px; line-height: 1.4; font-weight: 700; }
  .contact-lines span { font-weight: 400; }

  .tagline {
    left: 522px; top: 345px; color: var(--white);
    font-size: 22px; font-weight: 700; line-height: 1.2;
  }
  .front-brand { left: 495px; width: 495px; top: 455px; text-align: center; }
  .front-mark { font-size: 64px; color: var(--navy); margin-bottom: 10px; }
  .front-name { color: var(--navy); font-weight: 900; font-size: 27px; letter-spacing: 0.5px; }
  .front-sub { color: var(--grey); font-size: 22px; }
</style>
</head>
<body>
<main class="spread">
  <svg class="spread-art" width="990" height="700" viewBox="0 0 990 700" aria-hidden="false">
    <defs>
      <linearGradient id="paper-back" x1="0" y1="0" x2="1" y2="0">
        <stop offset="0" stop-color="var(--paper-shade)"/>
        <stop offset="1" stop-color="var(--paper)"/>
      </linearGradient>
      <linearGradient id="towers" x1="0" y1="0" x2="1" y2="1">
        <stop offset="0" stop-color="#c9d6ee"/>
        <stop offset="0.45" stop-color="#3f6bc4"/>
        <stop offset="1" stop-color="#1f3a8a"/>
      </linearGradient>
      <linearGradient id="house" x1="0" y1="0" x2="0" y2="1">
        <stop offset="0" stop-color="#7fb2ea"/>
        <stop offset="0.55" stop-color="#8a9ab8"/>
        <stop offset="1" stop-color="#4f8a3c"/>
      </linearGradient>
    </defs>

    <!-- back cover -->
    <rect class="page-back" x="0" y="0" width="495" height="700" fill="url(#paper-back)"/>
    <rect x="0" y="0" width="495" height="22" fill="var(--blue)"/>
    <path role="img" aria-label="Photo of glass office towers against a blue sky"
          d="M0,22 H495 V290 C455,290 420,292 380,330 C300,420 150,480 0,470 Z" fill="url(#towers)"/>
    <path class="back-band" d="M0,470 C150,480 300,420 380,330 C420,292 455,290 495,290 V420 C380,470 200,560 0,560 Z" fill="var(--blue)"/>
    <path d="M300,405 C360,340 420,300 495,296 V312 C430,318 370,360 300,405 Z" fill="var(--band-light)"/>

    <!-- front cover -->
    <rect class="page-front" x="495" y="0" width="495" height="700" fill="var(--paper)"/>
    <rect x="495" y="0" width="495" height="22" fill="var(--blue)"/>
    <path role="img" aria-label="Photo of a large suburban family home with garden and driveway"
          d="M495,22 H990 V320 C900,350 800,345 700,320 C620,300 560,280 495,290 Z" fill="url(#house)"/>
    <path class="front-band" d="M495,290 C560,280 620,300 700,320 C800,345 900,350 990,320 V352 C850,380 700,430 495,435 Z" fill="var(--blue)"/>
    <path d="M495,290 C560,280 620,300 700,320 C780,340 860,346 930,338 C850,338 780,326 700,308 C620,290 560,276 495,283 Z" fill="var(--sky)"/>
    <line x1="495" y1="0" x2="495" y2="700" stroke="#000" stroke-opacity="0.08" stroke-width="2"/>
  </svg>

  <div class="text brand-mark back-mark">HRE</div>

  <section class="text contact">
    <h2 class="contact-title">Contact Us:</h2>
    <p class="contact-address">Messrs. HRE | Management Consulting<br>Unit 3 of Plot No. 2187<br>Meridian Avenue, Kafue, Lusaka</p>
    <p class="contact-lines">Mobile: <span>+260 970 000 123/ 0960 000 456</span><br>E-mail: <span>info@holverypropertyconsultants.com</span></p>
  </section>

  <p class="text tagline">Accelerate<br>Success....</p>

  <section class="text front-brand">
    <div class="brand-mark front-mark">HRE</div>
    <h1 class="front-name">HOLVERY REAL ESTATE</h1>
    <p class="front-sub">Management Consulting</p>
  </section>
</main>
</body>
</html>
```